Commercial Refrigeration Service Company requires stylish and fresh looking flyer.

We need a flyer to hand out to new customers. It should have a photo and our branding, list all the services that are offered and our contact details.
We would like two flyers to be supplied, both identical though one offering a discount until July ( Half Price Service Fee ). The flyer should be clear, interesting and in similar colours to the branding package supplied.
Please look at our website for information about the services on offer:
www.brambo-cooling.com.au

Target Market(s)

Cafes, bars, restaurants, pubs ect.

Font styles to use
Other font styles liked:
• Font package provided

Colors
85cae6
ffffff
333333

Requirements
Must have
• - The photo provided.
• - The company logo.
• - Similar feel to the website & business card.
• - Smooth layout and clear to understand.
Should not have
• - No clunky badges or prints.

```html
<!DOCTYPE html>
<html lang="en">
<head>
<meta charset="utf-8">
<title>Brambo Commercial Refrigeration Flyer</title>
<link href="https://fonts.googleapis.com/css2?family=Quicksand:wght@400;500&family=Open+Sans:wght@400;600&family=Oswald:wght@300;700&family=Dancing+Script:wght@600&display=swap" rel="stylesheet">
<style>
:root{
  --sky:#12a9ea;
  --brand-blue:#85cae6;
  --bright-blue:#5bc8f2;
  --navy-band:#1f4aa0;
  --charcoal:#2b2e31;
  --ink:#333333;
  --white:#ffffff;
  --stage:#e9e6e1;
}
*{margin:0;padding:0;box-sizing:border-box}
html,body{width:932px;height:1200px;overflow:hidden;background:var(--stage)}
.flyer{position:absolute;left:88px;top:71px;width:755px;height:1058px;background:var(--charcoal);overflow:hidden;box-shadow:0 2px 8px rgba(0,0,0,.2)}
.hero-photo{position:absolute;left:0;top:0;width:755px;height:502px;
  background:linear-gradient(180deg,var(--sky) 0%,#4fb7e4 36%,#7c8590 56%,#5d6470 80%,#3c4148 100%)}
.headline{position:absolute;left:41px;top:40px;color:var(--white);font-family:"Quicksand",sans-serif;font-weight:500;font-size:44px;line-height:52px;letter-spacing:.3px}
.tagline{position:absolute;left:41px;top:148px;color:var(--white);font-family:"Quicksand",sans-serif;font-size:28px}
.info-band{position:absolute;left:0;top:502px;width:755px;height:58px;background:var(--navy-band)}
.band-text{position:absolute;top:512px;color:var(--white);font-family:"Quicksand",sans-serif;font-weight:500;font-size:15px;line-height:20px}
.address{left:368px}.registration{left:574px}
.brand-column{position:absolute;left:51px;top:482px;width:285px;height:576px;background:var(--white);text-align:center;color:var(--ink)}
.brand-column > *{position:absolute;left:0;width:100%}
.brand-head{top:0;height:78px;background:var(--bright-blue);display:flex;align-items:center;justify-content:center;gap:10px}
.brand-name{font-family:"Quicksand",sans-serif;font-weight:500;font-size:32px;color:var(--ink)}
.brand-dot{width:12px;height:12px;border-radius:50%;background:var(--ink)}
.service-hours{top:158px;font-family:"Oswald",sans-serif;font-weight:300;font-size:27px;line-height:40px;color:#555}
.sales{top:206px;font-family:"Oswald",sans-serif;font-weight:700;font-size:38px;line-height:40px;color:var(--brand-blue)}
.follow{top:343px;font-family:"Dancing Script",cursive;font-size:20px;line-height:26px;color:#777}
.social{top:383px;display:flex;justify-content:center;gap:7px}
.social span{width:31px;height:31px;border-radius:50%;background:var(--navy-band)}
.social span:nth-child(2){background:#6b6b6b}
.social span:nth-child(3){background:var(--bright-blue)}
.contact-lead{top:445px;font-family:"Open Sans",sans-serif;font-size:16px;line-height:22px}
.phone{top:475px;font-family:"Oswald",sans-serif;font-weight:700;font-size:42px;line-height:50px;color:var(--ink)}
.email{top:524px;font-family:"Open Sans",sans-serif;font-size:16px;line-height:22px}
.services{position:absolute;left:362px;top:574px;width:370px;color:var(--white);font-family:"Open Sans",sans-serif}
.services h2{font-family:"Quicksand",sans-serif;font-weight:400;font-size:31px;color:var(--bright-blue);margin-bottom:10px}
.services ul{list-style:none}
.services li{font-weight:600;font-size:18px;line-height:24px;display:flex;align-items:center}
.services li svg{margin:0 10px 0 5px;flex:none}
.services p{font-size:14px;line-height:18px;text-align:justify;margin-top:18px}
.services p:first-of-type{margin-top:0;padding-top:34px}
.website{position:absolute;left:362px;top:986px;font-family:"Open Sans",sans-serif;font-weight:600;font-size:31px;color:var(--bright-blue)}
</style>
</head>
<body>
<main class="flyer">
  <div class="hero-photo" role="img" aria-label="Photo of the technician leaning on the branded service ute by the beach"></div>
  <h1 class="headline">COMMERCIAL REFRIGERATION<br>&amp; ELECTRICAL SERVICES</h1>
  <p class="tagline">ice makers &amp; beer systems</p>

  <div class="info-band"></div>
  <p class="band-text address">PO Box 4417 Wavecrest,<br>NSW 2099</p>
  <p class="band-text registration">ABN: 12 345 678 901<br>Licence No: 401122B</p>

  <aside class="brand-column">
    <div class="brand-head"><span class="brand-dot"></span><span class="brand-name">Brambo</span></div>
    <div class="service-hours">24 HR SERVICE</div>
    <div class="sales">SALES &amp;<br>INSTALLATIONS</div>
    <div class="follow">Follow us on:</div>
    <div class="social"><span></span><span></span><span></span></div>
    <div class="contact-lead">Get in touch with Dean</div>
    <div class="phone">0400 517 284</div>
    <div class="email">info@brambo-cooling.com.au</div>
  </aside>

  <section class="services">
    <h2>Our Services</h2>
    <ul>
      <li><svg width="15" height="15" viewBox="0 0 16 16"><circle cx="8" cy="8" r="8" fill="#5bc8f2"/><path d="M4.5 8.3l2.3 2.3 4.7-4.9" stroke="#fff" stroke-width="1.8" fill="none"/></svg>Commercial Refrigeration</li>
      <li><svg width="15" height="15" viewBox="0 0 16 16"><circle cx="8" cy="8" r="8" fill="#5bc8f2"/><path d="M4.5 8.3l2.3 2.3 4.7-4.9" stroke="#fff" stroke-width="1.8" fill="none"/></svg>Ice makers</li>
      <li><svg width="15" height="15" viewBox="0 0 16 16"><circle cx="8" cy="8" r="8" fill="#5bc8f2"/><path d="M4.5 8.3l2.3 2.3 4.7-4.9" stroke="#fff" stroke-width="1.8" fill="none"/></svg>Beer Systems</li>
      <li><svg width="15" height="15" viewBox="0 0 16 16"><circle cx="8" cy="8" r="8" fill="#5bc8f2"/><path d="M4.5 8.3l2.3 2.3 4.7-4.9" stroke="#fff" stroke-width="1.8" fill="none"/></svg>Electrical</li>
      <li><svg width="15" height="15" viewBox="0 0 16 16"><circle cx="8" cy="8" r="8" fill="#5bc8f2"/><path d="M4.5 8.3l2.3 2.3 4.7-4.9" stroke="#fff" stroke-width="1.8" fill="none"/></svg>24hr Service</li>
      <li><svg width="15" height="15" viewBox="0 0 16 16"><circle cx="8" cy="8" r="8" fill="#5bc8f2"/><path d="M4.5 8.3l2.3 2.3 4.7-4.9" stroke="#fff" stroke-width="1.8" fill="none"/></svg>Sales</li>
      <li><svg width="15" height="15" viewBox="0 0 16 16"><circle cx="8" cy="8" r="8" fill="#5bc8f2"/><path d="M4.5 8.3l2.3 2.3 4.7-4.9" stroke="#fff" stroke-width="1.8" fill="none"/></svg>Installations</li>
    </ul>
    <p>Brambo is completely paperless and uses cloud based trade service software to build a complete profile of your venue and equipment, allowing Dean to offer tailored advice for your business.</p>
    <p>Receive a text message when a technician is on their way and your invoice straight to your email at time of service. Pay with card, cash or cheque on site or online.</p>
  </section>
  <div class="website">brambo-cooling.com.au</div>
</main>
</body>
</html>
```